Flyer-Design für Infoblatt artgerechte Haltung Meerschweinchen
Zielgruppe
Pfotenkorb-Laden bietet Futter und Zubehör für Meerschweinchen, Kaninchen und andere Nager. Gerne möchte ich auch ein Infoblatt für artgerechte Meerschweinchen anbieten
Aufgabenstellung
Text muss so wie im PDF (InfoblattMeerschweinchen) vorhanden sein

```html
<!DOCTYPE html>
<html lang="de">
<head>
<meta charset="utf-8">
<title>Infoblatt kleines Meerschweinchen</title>
<link rel="stylesheet" href="https://fonts.googleapis.com/css2?family=Open+Sans:wght@400;600;700&family=Great+Vibes&display=swap">
<style>
  :root {
    --bg: #d9d9db;
    --paper: #ffffff;
    --green: #94a413;
    --green-dark: #6d7a0e;
    --text: #5a6410;
    --photo-a: #8a5a2e;
    --photo-b: #c9b48e;
  }
  * { box-sizing: border-box; margin: 0; padding: 0; }
  html, body { width: 1200px; height: 899px; overflow: hidden; }
  body {
    background: var(--bg);
    font-family: "Open Sans", sans-serif;
    position: relative;
  }
  .page {
    position: absolute;
    top: 166px;
    width: 400px;
    height: 566px;
    background: var(--paper);
    box-shadow: 0 6px 18px rgba(0,0,0,.18);
  }
  .page--front { left: 170px; }
  .page--back { left: 630px; }
  .block { position: absolute; background: var(--green); }
  .brand {
    position: absolute;
    left: 130px; width: 140px;
    display: flex; align-items: center; justify-content: center; gap: 6px;
    font-weight: 700; font-size: 15px; color: var(--green-dark);
    white-space: nowrap;
  }
  .brand__dot { width: 12px; height: 12px; border-radius: 50%; background: var(--green); flex: none; }
  .photo {
    position: absolute; left: 22px; top: 104px; width: 356px; height: 170px;
    background: radial-gradient(ellipse at 40% 55%, var(--photo-a) 0%, #6e4322 45%, var(--photo-b) 100%);
  }
  .cover-panel {
    position: absolute; left: 22px; top: 282px; width: 356px; height: 266px;
    background: var(--green); color: #fff;
  }
  .title { position: absolute; left: 30px; top: 18px; line-height: 1; }
  .title__small { font-family: "Great Vibes", cursive; font-size: 26px; position: absolute; left: 150px; top: 0; }
  .title__main { font-family: "Great Vibes", cursive; font-size: 58px; display: block; padding-top: 20px; }
  .title__label { font-size: 13px; font-weight: 600; display: block; margin: 2px 0 0 80px; }
  .cover-lead { position: absolute; left: 60px; top: 150px; font-size: 15px; line-height: 1.25; }
  .url-tab {
    position: absolute; background: var(--paper); color: var(--green-dark);
    font-weight: 700; font-size: 12px; display: flex; align-items: center; justify-content: center;
  }
  .page--front .url-tab { left: 88px; bottom: 0; width: 180px; height: 34px; }
  .info-box {
    position: absolute; left: 22px; top: 108px; width: 356px; height: 196px;
    border: 1px solid var(--green); padding: 12px 14px; color: var(--text);
  }
  .info-box h2 { font-size: 9.5px; font-weight: 700; line-height: 1.3; text-transform: uppercase; margin-bottom: 8px; }
  .info-cols { column-count: 2; column-gap: 16px; font-size: 8px; line-height: 1.4; text-align: justify; }
  .info-cols p { margin-bottom: 7px; }
  .back-panel { position: absolute; left: 22px; top: 312px; width: 356px; height: 236px; background: var(--green); }
  .page--back .url-tab { left: 88px; top: 0; width: 180px; height: 38px; }
  .contact {
    position: absolute; right: 26px; bottom: 34px; color: #fff;
    font-size: 10.5px; font-weight: 600; line-height: 1.45;
    border-bottom: 1px solid #fff; padding-bottom: 8px; width: 150px;
  }
  .contact__row { display: flex; align-items: center; gap: 5px; }
  .contact svg { width: 10px; height: 10px; flex: none; }
</style>
</head>
<body>

<section class="page page--front">
  <div class="block" style="left:22px;top:18px;width:116px;height:48px"></div>
  <div class="block" style="left:262px;top:52px;width:116px;height:44px"></div>
  <div class="brand" style="top:30px"><span class="brand__dot"></span>Pfotenkorb-Laden</div>
  <div class="photo" role="img" aria-label="Foto: Nahaufnahme eines braunen langhaarigen Meerschweinchens im Heu"></div>
  <div class="cover-panel">
    <div class="title">
      <span class="title__small">kleines</span>
      <span class="title__main">Meerschweinchen</span>
      <span class="title__label">Infoblatt</span>
    </div>
    <p class="cover-lead">Was man alles über<br>Meerschweinchen<br>wissen sollte</p>
    <div class="url-tab">www.pfotenkorb-laden.ch</div>
  </div>
</section>

<section class="page page--back">
  <div class="block" style="left:262px;top:18px;width:116px;height:48px"></div>
  <div class="block" style="left:22px;top:56px;width:116px;height:44px"></div>
  <div class="brand" style="top:42px"><span class="brand__dot"></span>Pfotenkorb-Laden</div>
  <div class="info-box">
    <h2>Aufklärung, Beratung bei Fragen oder Problemen rund um die Meerschweinchenhaltung:</h2>
    <div class="info-cols">
      <p>Meerschweinchen haben wenig Ansprüche, lassen sich leicht in einem kleinen Käfig halten, der wenig Platz braucht und sind in Einzelhaltung geeignete Kuscheltiere für Kinder. Sie sind mit Grünabfällen kostengünstig zu füttern.</p>
      <p>Aussagen, die man immer noch viel zu häufig hört! Doch diese Aussagen sind falsch. Als Haustiere erfreuen sich Meerschweinchen in den letzten Jahren einer immer grösseren Beliebtheit. Leider steht das Meerschweinchen in dem Ruf ein anspruchsloses, pflegeleichtes Schmusetier zu sein. Was bei weitem nicht der Fall ist. Auch Meerschweinchen haben Ansprüche, sind in Einzelhaft unglücklich und brauchen qualitatives Heu und Grünfutter. Sie sind äusserst bewegungsfreudig und ein kleiner Käfig wird schnell zum Gefängnis.</p>
      <p>Wir stehen Ihnen für alle Haltungs-, Pflege- und Ernährungsfragen jederzeit zur Verfügung.</p>
    </div>
  </div>
  <div class="back-panel">
    <div class="url-tab">www.pfotenkorb-laden.ch</div>
    <address class="contact" style="font-style:normal">
      <div>Mara Lindholz</div>
      <div>Ahornstrasse 8</div>
      <div>4600 Talhausen</div>
      <div class="contact__row">
        <svg viewBox="0 0 10 10" aria-hidden="true"><path d="M2 1l2 2-1 1.2c.6 1.2 1.6 2.2 2.8 2.8L7 6l2 2-1.3 1.3C4.5 9 1 5.5.7 2.3z" fill="#fff"/></svg>
        +41 (0)00 100 20 30</div>
      <div class="contact__row">
        <svg viewBox="0 0 10 10" aria-hidden="true"><path d="M2 1l2 2-1 1.2c.6 1.2 1.6 2.2 2.8 2.8L7 6l2 2-1.3 1.3C4.5 9 1 5.5.7 2.3z" fill="#fff"/></svg>
        +41 (0)00 400 50 60</div>
      <div class="contact__row">
        <svg viewBox="0 0 10 10" aria-hidden="true"><rect x=".5" y="2" width="9" height="6" fill="#fff"/><path d="M.5 2l4.5 3.5L9.5 2" fill="none" stroke="#94a413" stroke-width=".9"/></svg>
        info@pfotenkorb-laden.ch</div>
    </address>
  </div>
</section>

</body>
</html>
```